Bright Fern Property Services

Design a billboard with our logo that includes bullet points for
Property Maintenance, Plumbing, and Electrical, licensed and insured.
Phone number 865 418 3907

also add the website brightfernps-example.com

```html
<!DOCTYPE html>
<html lang="en">
<head>
<meta charset="utf-8">
<title>Bright Fern Property Services Billboard</title>
<link rel="stylesheet" href="https://fonts.googleapis.com/css2?family=Montserrat:wght@500;600;700;800&display=swap">
<style>
  :root {
    --green: #4caf50;
    --ink: #111111;
    --white: #ffffff;
    --stage: #e6e6e6;
    --panel-grey: #eeeeee;
    --ring-grey: #d9d9d9;
    --house-photo: #b9c8c0;
    --window-photo: #8a8f86;
    --pipe-photo: #c8ccd0;
    --panel-photo: #5e6770;
  }
  * { box-sizing: border-box; margin: 0; padding: 0; }
  html, body {
    width: 1200px; height: 463px; overflow: hidden;
    background: var(--stage);
    font-family: "Montserrat", Arial, sans-serif;
  }
  .billboard {
    position: absolute; left: 0; top: 45px;
    width: 1200px; height: 372px;
    background: var(--white);
    overflow: hidden;
  }
  .brand {
    position: absolute; left: 44px; top: 26px;
    display: flex; align-items: center; gap: 12px;
  }
  .brand-dot {
    width: 22px; height: 22px; border-radius: 50%;
    background: var(--green);
  }
  .brand-name {
    color: var(--green); font-weight: 800;
    font-size: 25px; line-height: 30px; letter-spacing: 0.5px;
  }
  .badge {
    position: absolute; left: 537px; top: 85px;
    width: 205px; height: 24px;
    border: 1.5px solid var(--green); border-radius: 12px;
    font-size: 14.5px; font-weight: 700; color: var(--ink);
    display: flex; align-items: center; justify-content: center;
  }
  .headline {
    position: absolute; left: 49px; top: 150px;
    color: var(--green); font-weight: 800;
    font-size: 38px; line-height: 47px; letter-spacing: 0.2px;
    text-transform: uppercase;
  }
  .services {
    position: absolute; top: 260px; left: 50px; right: 0; height: 36px;
    list-style: none;
  }
  .service {
    position: absolute; top: 0; display: flex; align-items: center; gap: 8px;
    font-size: 23.5px; font-weight: 600; color: var(--ink);
  }
  .service svg { width: 35px; height: 35px; flex: none; }
  .service.maintenance { left: 0; }
  .service.plumbing { left: 344px; }
  .service.electrical { left: 540px; }
  .call-bar {
    position: absolute; left: 0; top: 318px; width: 460px; height: 54px;
  }
  .call-bar svg.bar-shape { position: absolute; inset: 0; }
  .call-text {
    position: absolute; left: 62px; top: 0; height: 54px;
    display: flex; align-items: center; gap: 12px;
    color: var(--white); font-size: 29px; font-weight: 500;
  }
  .call-text strong { font-weight: 700; }
  .call-text svg { width: 26px; height: 26px; }
  .website {
    position: absolute; left: 474px; top: 331px;
    font-size: 17px; font-weight: 600; color: var(--ink);
    white-space: nowrap;
  }
  .website span { color: var(--green); font-weight: 700; }
  .base-line {
    position: absolute; left: 460px; right: 0; top: 365px; height: 7px;
    background: var(--green);
  }
  .photo-panel {
    position: absolute; left: 770px; top: 0; width: 430px; height: 372px;
    background: linear-gradient(135deg, #ffffff 0%, var(--panel-grey) 60%, #f7f7f7 100%);
  }
  .photo-art { position: absolute; left: 760px; top: 0; }
</style>
</head>
<body>
  <main class="billboard">
    <div class="photo-panel"></div>

    <div class="brand">
      <div class="brand-dot"></div>
      <div class="brand-name">Bright Fern<br>Property Services</div>
    </div>

    <div class="badge">Licensed and Insured</div>

    <h1 class="headline">Dependable property care<br>for peace of mind</h1>

    <ul class="services">
      <li class="service maintenance">
        <svg viewBox="0 0 36 36"><circle cx="18" cy="18" r="17" fill="var(--green)" stroke="var(--ink)" stroke-width="1"/><path d="M9 18 L18 10 L27 18 V26 H9 Z" fill="var(--ink)"/><rect x="16" y="20" width="4" height="6" fill="var(--green)"/></svg>
        Property Maintenance
      </li>
      <li class="service plumbing">
        <svg viewBox="0 0 36 36"><circle cx="18" cy="18" r="17" fill="var(--green)" stroke="var(--ink)" stroke-width="1"/><path d="M11 10 V24 a3 3 0 0 0 3 3 h2 V16 h4 v11 h2 a3 3 0 0 0 3 -3 V14" fill="none" stroke="var(--ink)" stroke-width="3"/></svg>
        Plumbing
      </li>
      <li class="service electrical">
        <svg viewBox="0 0 36 36"><circle cx="18" cy="18" r="17" fill="var(--green)" stroke="var(--ink)" stroke-width="1"/><circle cx="18" cy="18" r="11" fill="none" stroke="var(--ink)" stroke-width="2"/><path d="M20 9 L13 20 H18 L16 27 L23 16 H18 Z" fill="var(--ink)"/></svg>
        Electrical
      </li>
    </ul>

    <div class="call-bar">
      <svg class="bar-shape" viewBox="0 0 460 54" preserveAspectRatio="none"><path d="M0 0 H425 Q438 0 442 12 L460 54 H0 Z" fill="var(--ink)"/></svg>
      <div class="call-text">
        <svg viewBox="0 0 26 26"><circle cx="13" cy="13" r="12" fill="var(--green)"/><path d="M9 7 l2.5 0 l1 3.5 l-1.5 1.2 a8 8 0 0 0 3.3 3.3 l1.2 -1.5 l3.5 1 l0 2.5 a1.5 1.5 0 0 1 -1.5 1.5 A11 11 0 0 1 7.5 8.5 A1.5 1.5 0 0 1 9 7 Z" fill="var(--white)"/></svg>
        <span>Call us <strong>865 418 3907</strong></span>
      </div>
    </div>

    <div class="website">www.<span>brightfernps-example</span>.com</div>
    <div class="base-line"></div>

    <svg class="photo-art" width="440" height="372" viewBox="760 0 440 372">
      <circle cx="979" cy="135" r="184" fill="var(--ring-grey)"/>
      <circle cx="979" cy="135" r="178" fill="var(--house-photo)" role="img" aria-label="Photo of a large white house with a green lawn"/>
      <g>
        <circle cx="855" cy="220" r="61" fill="var(--white)"/>
        <circle cx="855" cy="220" r="57" fill="var(--green)"/>
        <circle cx="855" cy="220" r="54" fill="var(--window-photo)" role="img" aria-label="Photo of a worker sealing a window frame"/>
      </g>
      <g>
        <circle cx="1108" cy="220" r="62" fill="var(--white)"/>
        <circle cx="1108" cy="220" r="58" fill="var(--green)"/>
        <circle cx="1108" cy="220" r="55" fill="var(--pipe-photo)" role="img" aria-label="Photo of hands repairing a sink drain pipe"/>
      </g>
      <g>
        <circle cx="980" cy="273" r="66" fill="var(--white)"/>
        <circle cx="980" cy="273" r="62" fill="var(--green)"/>
        <circle cx="980" cy="273" r="59" fill="var(--panel-photo)" role="img" aria-label="Photo of an electrician testing a breaker panel with a multimeter"/>
      </g>
    </svg>
  </main>
</body>
</html>
```